Moving comapny Postcard mailer Design

I am looking for a 6x9 postcard with real images of our team. I would like to add the same review we currently have , I want the colors of the postcard to be orange and white. I want the team picture to be enlarged with the other pictures to be mimized. I will add example postcards to give rough ideas. My company is called Harlow Moving and the postcards with that name are our current postcards. The additional postcards are from other companies who have better postcards than mine. My goal is for my postcard to be better that theirs.

Target Market(s)

Wealthy people in the 35+ age group

Industry/Entity Type

Moving company

Requirements
Must have
• Beauty

```html
<!DOCTYPE html>
<html lang="en">
<head>
<meta charset="utf-8">
<title>Harlow Moving — Postcard Mailer</title>
<link href="https://fonts.googleapis.com/css2?family=Montserrat:wght@600;700;800&family=Open+Sans:ital,wght@0,400;0,600;1,400&display=swap" rel="stylesheet">
<style>
  :root {
    --red: #d63c26;
    --dark: #2d2b2c;
    --white: #ffffff;
    --backdrop: #e6e6e6;
    --ink: #222222;
    --photo-team-a: #5b6b48;
    --photo-team-b: #3a3a3a;
    --photo-house-a: #8e9097;
    --photo-house-b: #6f6457;
  }
  html, body { margin: 0; padding: 0; overflow: hidden; }
  body { width: 947px; height: 1200px; background: var(--backdrop); }
  .stage {
    position: relative; width: 960px; height: 1216px;
    transform: scale(0.9865); transform-origin: 0 0;
  }
  .card {
    position: absolute; left: 75px; width: 810px; height: 539px;
    background: var(--white); overflow: hidden;
    font-family: "Montserrat", sans-serif;
  }
  .card--front { top: 54px; }
  .card--back { top: 629px; }
  .layer { position: absolute; left: 0; top: 0; }
  .abs { position: absolute; }

  .headline {
    right: 40px; top: 62px; margin: 0; color: var(--white);
    font-weight: 700; font-size: 64px; line-height: 1.1; text-align: left;
  }
  .brand {
    display: flex; align-items: center; gap: 10px;
    color: var(--dark); font-weight: 800; font-size: 22px; line-height: 1;
    letter-spacing: 0.5px;
  }
  .brand__mark { width: 30px; height: 30px; background: var(--red); flex: none; }
  .brand__name { width: 110px; }

  .offers { display: flex; gap: 1px; }
  .offer { position: relative; width: 135px; height: 118px; }
  .offer svg { position: absolute; left: 0; top: 0; }
  .offer__price {
    position: absolute; left: 18px; top: 8px; width: 66px; text-align: center;
    color: var(--white); font-weight: 700; font-size: 22px; line-height: 1;
  }
  .offer__price sup { font-size: 12px; vertical-align: 9px; }
  .offer__price small { display: block; font-size: 7px; font-weight: 700; margin-top: 1px; }
  .offer__terms {
    position: absolute; left: 0; top: 67px; width: 135px; text-align: center;
    color: var(--white); font-family: "Open Sans", sans-serif; font-size: 9px; line-height: 12px;
  }

  .cta { margin: 0; font-family: "Open Sans", sans-serif; font-style: italic; font-size: 15px; color: var(--ink); }
  .phone { margin: 0; color: var(--red); font-weight: 700; font-size: 39px; letter-spacing: 0.5px; line-height: 1; }
  .web {
    margin: 0; color: var(--white); font-family: "Open Sans", sans-serif;
    font-size: 15px; letter-spacing: 3px;
  }
  .slogan {
    margin: 0; color: var(--white); font-weight: 700; font-size: 29px; line-height: 31px;
  }
  .stamp { border: 1.5px solid var(--dark); width: 88px; height: 101px; box-sizing: border-box; }
  .address-line { height: 0; border-top: 1px solid var(--dark); width: 256px; }
</style>
</head>
<body>
<div class="stage">

  <!-- FRONT -->
  <section class="card card--front">
    <svg class="layer" width="440" height="415" role="img" aria-label="Photo of the moving crew posing in the back of a box truck">
      <defs>
        <linearGradient id="teamPhoto" x1="0" y1="0" x2="0" y2="1">
          <stop offset="0" stop-color="var(--photo-team-a)"/>
          <stop offset="0.55" stop-color="var(--photo-team-b)"/>
          <stop offset="1" stop-color="#7a7a78"/>
        </linearGradient>
      </defs>
      <rect width="440" height="415" fill="url(#teamPhoto)"/>
    </svg>
    <svg class="layer" width="810" height="539">
      <polygon points="300,0 810,0 810,232 782,268 430,268" fill="var(--red)"/>
      <polygon points="0,415 390,415 420,440 390,476 0,476" fill="var(--white)"/>
      <polygon points="445,415 810,415 810,476 445,476" fill="var(--white)"/>
      <rect x="250" y="501" width="195" height="12" fill="var(--dark)"/>
      <polygon points="0,521 430,521 452,496 810,496 810,539 0,539" fill="var(--red)"/>
    </svg>
    <svg class="abs" style="left:243px;top:349px" width="140" height="130" role="img" aria-label="Photo of a mover wheeling wrapped furniture on a dolly">
      <polygon points="35,2 105,2 138,65 105,128 35,128 2,65" fill="#6d7a63" stroke="var(--white)" stroke-width="4"/>
    </svg>

    <h1 class="abs headline">HARLOW<br>MOVING</h1>

    <div class="abs brand" style="left:40px;top:443px">
      <span class="brand__mark"></span><span class="brand__name">HARLOW MOVING</span>
    </div>

    <div class="abs offers" style="left:382px;top:286px">
      <div class="offer">
        <svg width="135" height="118"><polygon points="25,0 110,0 135,59 110,118 25,118 0,59" fill="var(--dark)"/><polygon points="25,0 98,0 73,52 0,52 0,59" fill="var(--red)"/></svg>
        <div class="offer__price"><sup>$</sup>25<small>OFF</small></div>
        <div class="offer__terms">Moves Under<br>$1000<br>With this card.</div>
      </div>
      <div class="offer">
        <svg width="135" height="118"><polygon points="25,0 110,0 135,59 110,118 25,118 0,59" fill="var(--dark)"/><polygon points="25,0 98,0 73,52 0,52 0,59" fill="var(--red)"/></svg>
        <div class="offer__price"><sup>$</sup>50<small>OFF</small></div>
        <div class="offer__terms">Moves Over<br>$1000<br>With this card.</div>
      </div>
      <div class="offer">
        <svg width="135" height="118"><polygon points="25,0 110,0 135,59 110,118 25,118 0,59" fill="var(--dark)"/><polygon points="25,0 98,0 73,52 0,52 0,59" fill="var(--red)"/></svg>
        <div class="offer__price"><sup>$</sup>100<small>OFF</small></div>
        <div class="offer__terms">Moves Over<br>$3000<br>With this card.</div>
      </div>
    </div>

    <p class="abs cta" style="right:38px;top:423px">Call us today to get started!</p>
    <p class="abs phone" style="right:40px;top:446px">865-555-0142</p>
    <p class="abs web" style="right:38px;top:506px">www.harlowmovers.com</p>
  </section>

  <!-- BACK -->
  <section class="card card--back">
    <svg class="layer" width="360" height="250" role="img" aria-label="Photo of movers carrying plastic-wrapped furniture out of a house">
      <defs>
        <linearGradient id="housePhoto" x1="0" y1="0" x2="1" y2="1">
          <stop offset="0" stop-color="var(--photo-house-a)"/>
          <stop offset="0.6" stop-color="var(--photo-house-b)"/>
          <stop offset="1" stop-color="#6f8a55"/>
        </linearGradient>
      </defs>
      <polygon points="0,0 350,0 290,250 0,250" fill="url(#housePhoto)"/>
    </svg>
    <svg class="layer" width="810" height="539">
      <polygon points="312,114 510,114 456,226 258,226" fill="var(--red)"/>
      <polygon points="0,496 345,496 368,521 810,521 810,539 0,539" fill="var(--dark)"/>
    </svg>

    <div class="abs brand" style="left:372px;top:50px">
      <span class="brand__mark"></span><span class="brand__name">HARLOW MOVING</span>
    </div>
    <p class="abs slogan" style="left:292px;top:122px">MOVING.<br>MADE.<br>SIMPLE.</p>

    <div class="abs offers" style="left:20px;top:269px">
      <div class="offer">
        <svg width="135" height="118"><polygon points="25,0 110,0 135,59 110,118 25,118 0,59" fill="var(--dark)"/><polygon points="25,0 98,0 73,52 0,52 0,59" fill="var(--red)"/></svg>
        <div class="offer__price"><sup>$</sup>25<small>OFF</small></div>
        <div class="offer__terms">Moves Under<br>$1000<br>With this card.</div>
      </div>
      <div class="offer">
        <svg width="135" height="118"><polygon points="25,0 110,0 135,59 110,118 25,118 0,59" fill="var(--dark)"/><polygon points="25,0 98,0 73,52 0,52 0,59" fill="var(--red)"/></svg>
        <div class="offer__price"><sup>$</sup>50<small>OFF</small></div>
        <div class="offer__terms">Moves Over<br>$1000<br>With this card.</div>
      </div>
      <div class="offer">
        <svg width="135" height="118"><polygon points="25,0 110,0 135,59 110,118 25,118 0,59" fill="var(--dark)"/><polygon points="25,0 98,0 73,52 0,52 0,59" fill="var(--red)"/></svg>
        <div class="offer__price"><sup>$</sup>100<small>OFF</small></div>
        <div class="offer__terms">Moves Over<br>$3000<br>With this card.</div>
      </div>
    </div>

    <p class="abs cta" style="left:35px;top:415px">Call us today to get started!</p>
    <p class="abs phone" style="left:34px;top:442px">865-555-0142</p>
    <p class="abs web" style="left:35px;top:506px">www.harlowmovers.com</p>

    <div class="abs stamp" style="left:685px;top:96px"></div>
    <div class="abs address-line" style="left:517px;top:350px"></div>
    <div class="abs address-line" style="left:517px;top:400px"></div>
    <div class="abs address-line" style="left:517px;top:449px"></div>
  </section>

</div>
</body>
</html>
```